Lorvika.no is a new website about pedagogical entrepreneurship. It's main target group is teachers. The Fjellmark Institute for Classroom Media and the Nordvik Agency for Schools and Study are leading the project.

The web page is meant to show examples of how different methods of entrepreneurship can be used pedagogical in a learning environment. The page will also support the user with examples of different teaching programs and other examples of best practice.

Pedagogical entrepreneurship is not about business and men in suits. It's a method for learning. The focus in the design should be on school, education and new ways of learning.

The final product should be motivating and engaging, but at the same time governmental and serious. We are not looking for something "flashy" and corporate-looking, but a moderate, task-focused and clean design that state quality.

We need designs for three pages:
1 - frontpage
2 - subpage ("Metoder og undervisningsopplegg")
3 - subpage ("Smått-VERK i Brekkelia")

The interaction design for these three pages will be uploaded as an attachment.

We would like you to find inspiration in the following websites:
- www.gryvekst.no
- www.lavrek.no
- www.tovandstudio.com
- www.kvp.no
(more will be added)

Please use the attached logo, and feel free to use this as an inspiration for the rest of the design.

Target Market(s)

Teachers

Industry/Entity Type

Education

Requirements
Must have
• * Header with: Logo. Main navigation. Utility navigation. Search box.
* Footer
Should not have
• Images of men in suits.
Very strong graphical elements that stands out too much (we want it clean).

```html
<!DOCTYPE html>
<html lang="en">
<head>
<meta charset="utf-8">
<title>Lorvika – Pedagogical Entrepreneurship</title>
<link rel="stylesheet" href="https://fonts.googleapis.com/css2?family=Cabin:ital,wght@0,400;0,500;0,600;1,400;1,500&display=swap">
<style>
:root{
  --navy:#22305a;
  --blue:#0a78be;
  --blue-mid:#1f7cbf;
  --sky:#8fd0f5;
  --link:#7ec3f0;
  --paper:#ebebea;
  --footer:#1b4a7e;
  --line:#6aa0d0;
  --ink:#22305a;
  --white:#ffffff;
}
*{margin:0;padding:0;box-sizing:border-box}
html,body{width:1115px;height:1200px;overflow:hidden;background:var(--blue)}
body{font-family:"Cabin",sans-serif;color:var(--white)}
.page{position:absolute;left:0;top:0;width:1098px;height:1182px;transform:scale(1.0155);transform-origin:0 0;background:var(--blue)}
.abs{position:absolute}
.topbar{left:0;top:0;width:1098px;height:26px;background:var(--navy)}
.header{left:0;top:26px;width:1098px;height:186px;background:var(--paper)}
.brand{left:30px;top:66px;display:flex;align-items:center;gap:24px}
.brand-dot{width:90px;height:90px;border-radius:50%;background:var(--blue-mid)}
.brand-name{font-size:64px;font-weight:600;color:var(--blue-mid);line-height:1;letter-spacing:-1px;margin-top:-16px}
.brand-sub{left:158px;top:148px;font-size:14px;color:var(--blue-mid);white-space:nowrap}
.tagline{left:622px;top:86px;color:var(--ink);font-style:italic}
.tagline h2{font-size:22px;font-weight:400;letter-spacing:.3px;line-height:30px}
.tagline p{font-size:18px;line-height:25px}
.learn{display:inline-block;background:var(--navy);color:var(--white);font-style:italic;font-size:16px;padding:0 10px;margin-left:8px;line-height:22px}
.feature-panel{left:30px;top:257px;width:1040px;height:248px;background:var(--navy);border:1px solid var(--line)}
.feature{position:absolute;top:20px;width:240px;text-align:center}
.feature .art{width:120px;height:120px;margin:8px auto 0;border-radius:50%;background:radial-gradient(circle at 40% 35%,var(--sky),var(--blue-mid) 70%,var(--blue))}
.feature .kicker{margin-top:16px;font-size:11px;line-height:13px;color:#5a86b8}
.feature h3{font-size:17px;font-weight:400;line-height:18px;margin-top:2px}
.gauge-box{left:30px;top:535px;width:273px;height:221px;background:var(--navy);border:1px solid var(--line)}
.gauge-title{position:absolute;left:8px;top:7px;width:257px;height:43px;background:var(--blue-mid);text-align:center;font-size:17px;line-height:18px;padding-top:3px}
.gauge-art{position:absolute;left:82px;top:68px;width:110px;height:110px;border-radius:50%;background:radial-gradient(circle at 40% 35%,#e6f4fb,#7fb4d8 60%,#2a4b78)}
.gauge-btn{position:absolute;left:59px;top:189px;width:152px;height:22px;background:var(--blue-mid);font-size:14px;text-align:center;line-height:22px}
.start-panel{left:318px;top:535px;width:752px;height:221px;background:linear-gradient(180deg,#3aa6e6,#1f86c9);border:1px solid #1c6aa8}
.start-title{position:absolute;left:293px;top:11px;width:170px;height:43px;background:var(--navy);font-size:25px;text-align:center;line-height:43px;letter-spacing:.5px}
.start-inner{position:absolute;left:18px;top:77px;width:719px;height:126px;background:linear-gradient(180deg,#b5e2f8,#4cb0ea);border:1px solid #9ad2f2}
.col-title{position:absolute;font-size:16px;font-weight:500;color:var(--ink);text-align:center;width:200px}
.chip{position:absolute;width:114px;height:21px;background:var(--blue-mid);font-size:14px;text-align:center;line-height:21px}
.more{position:absolute;width:85px;height:17px;background:var(--navy);font-size:13px;text-align:center;line-height:17px}
.inspiration{left:30px;top:785px;width:1040px;height:178px;background:var(--paper);border:1px solid #c9d6e2}
.insp-label{position:absolute;left:5px;top:6px;width:115px;height:23px;background:var(--blue-mid);font-size:14px;line-height:23px;padding-left:21px}
.arrow{position:absolute;width:40px;height:40px}
.card{position:absolute;width:140px;text-align:center;color:var(--ink);font-size:14px;line-height:13px}
.card .photo{width:130px;height:88px;margin:0 auto 3px;background:linear-gradient(180deg,#c9d8e6 0%,#9aa6b2 45%,#b08060 70%,#eef1f3 100%)}
.footer{left:0;top:970px;width:1098px;height:186px;background:var(--footer)}
.footer-name{position:absolute;left:30px;top:76px;font-size:30px;font-weight:600;color:var(--white)}
.fcol{position:absolute;top:20px;text-align:center;width:220px}
.fcol h4{font-size:17px;font-weight:400;line-height:18px;height:48px;display:flex;align-items:flex-end;justify-content:center;padding-bottom:9px}
.fcol a{display:block;color:var(--link);text-decoration:none;font-size:14px;line-height:25px}
.bottombar{left:0;top:1156px;width:1098px;height:26px;background:var(--navy)}
</style>
</head>
<body>
<div class="page">
  <div class="abs topbar"></div>

  <header class="abs header"></header>
  <div class="abs brand"><span class="brand-dot"></span><span class="brand-name">Lorvika</span></div>
  <div class="abs brand-sub">Entreprenørielle metoder i undervisningen</div>
  <div class="abs tagline">
    <h2>Pedagogical Enterprenuership works.</h2>
    <p>Lorem ipsum dolor sit amet, erat in id vene,</p>
    <p>mauris diam sed. <span class="learn">Learn More &gt;</span></p>
  </div>

  <section class="abs feature-panel">
    <div class="feature" style="left:55px">
      <div class="art" role="img" aria-label="Speech bubble illustration with letters and a light bulb"></div>
      <div class="kicker">Learn about what, why and how!</div>
      <h3>What is Pedagogical<br>Enterpreneurship?</h3>
    </div>
    <div class="feature" style="left:415px">
      <div class="art" role="img" aria-label="Speech bubble illustration with a pen and paper"></div>
      <div class="kicker">Plan Your Lessons!</div>
      <h3>Methods &amp;<br>Teaching Plans</h3>
    </div>
    <div class="feature" style="left:745px">
      <div class="art" role="img" aria-label="Speech bubble illustration with a checked box"></div>
      <div class="kicker">Be Inspired!</div>
      <h3>Good Examples/<br>Best Practice</h3>
    </div>
  </section>

  <section class="abs gauge-box">
    <div class="gauge-title">Are You Working<br>Enterprenuership-Like?</div>
    <div class="gauge-art" role="img" aria-label="Gauge dial illustration"></div>
    <div class="gauge-btn">Try the Lorvimeter!</div>
  </section>

  <section class="abs start-panel">
    <div class="start-inner">
      <div class="col-title" style="left:55px;top:5px">Methods</div>
      <div class="chip" style="left:27px;top:38px">Cafe-Pedagogikk</div>
      <div class="chip" style="left:175px;top:38px">Grundercamp</div>
      <div class="chip" style="left:27px;top:69px">Elevbedrift</div>
      <div class="chip" style="left:175px;top:69px">Storyline</div>
      <div class="more" style="left:116px;top:104px">See More</div>
      <div class="col-title" style="left:467px;top:5px">Teaching Plans</div>
      <div class="chip" style="left:429px;top:38px">Plan 01</div>
      <div class="chip" style="left:578px;top:38px">Plan 02</div>
      <div class="chip" style="left:429px;top:69px">Plan 03</div>
      <div class="chip" style="left:578px;top:69px">Plan 04</div>
      <div class="more" style="left:519px;top:104px">See More</div>
    </div>
    <div class="start-title">Get Started</div>
  </section>

  <section class="abs inspiration">
    <div class="insp-label">Inspiration</div>
    <svg class="arrow" style="left:8px;top:68px" viewBox="0 0 40 40"><circle cx="20" cy="20" r="18" fill="none" stroke="#22305a" stroke-width="3"/><path d="M10 20 L27 11 L22 20 L27 29 Z" fill="#22305a"/></svg>
    <svg class="arrow" style="left:987px;top:66px" viewBox="0 0 40 40"><circle cx="20" cy="20" r="18" fill="none" stroke="#22305a" stroke-width="3"/><path d="M10 20 L27 11 L22 20 L27 29 Z" fill="#22305a"/></svg>
    <div class="card" style="left:75px;top:41px"><div class="photo" role="img" aria-label="Photo of a school yard in winter"></div>Smått-VERK - at<br>Brekkelia School</div>
    <div class="card" style="left:334px;top:41px"><div class="photo" role="img" aria-label="Photo of a school yard in winter"></div>Smått-VERK - at<br>Brekkelia School</div>
    <div class="card" style="left:580px;top:39px"><div class="photo" role="img" aria-label="Photo of a school yard in winter"></div>Smått-VERK - at<br>Brekkelia School</div>
    <div class="card" style="left:818px;top:39px"><div class="photo" role="img" aria-label="Photo of a school yard in winter"></div>Smått-VERK - at<br>Brekkelia School</div>
  </section>

  <footer class="abs footer">
    <div class="footer-name">Lorvika</div>
    <nav class="fcol" style="left:207px"><h4>Pedagogical<br>Enterpreneurship</h4><a>What is it?</a><a>Science</a><a>Best Practice Schools</a></nav>
    <nav class="fcol" style="left:419px"><h4>Methods</h4><a>Cafe-Pedagogikk</a><a>Grundercamp</a><a>Storyline</a></nav>
    <nav class="fcol" style="left:605px"><h4>Teaching Plans</h4><a>Plan 01</a><a>Plan 02</a><a>Plan 03</a></nav>
    <nav class="fcol" style="left:793px;width:246px"><h4>Inspiration</h4><a>Smått-VERK - at Brekkelia School</a><a>Smått-VERK - at Brekkelia School</a><a>Smått-VERK - at Brekkelia School</a></nav>
  </footer>
  <div class="abs bottombar"></div>
</div>
</body>
</html>
```